Varnell Contracting In need of monthly newsletter

We need a monthly newsletter to promote our monthly special of Mulch Installation.

Please change wording to fit what you feel is professional and effective.

Our regular price to install Mulch is $169/Yard installed/Delivered

We would like to run a promotion of $125/Yard Installed & Delivered

Compare us to others $135/Yard Delivered only from some other suppliers

Also list somewhere on the newsletter :
- Delivery of soils, stone, wood also available
- Check out our website
- an emphasis on quality

The Fine Print
* Some Conditions apply
Mulches included in sale Onyx Velvet, Chocolate Brown, Auburn Red, Natural, Hemlock, Gold, Shredded Pine. Some site conditions may incur extra cost. minimum 3 Yards for sale price to be in effect, HST extra on all prices listed,

CHECK OUR WEBSITE FOR SOME IMAGES AND MORE INFORMATION....

ASK ANYTHING YOU WANT VIA Draft Plaza
Updates

Types of Mulch have changed Slightly in the "Fine Print"

Classic Cedar, Black Cedar, Red Cedar, Chocolate brown, Pine Bark, Natural Shredded Pine, Hemlock, Utility Style.

We will also be submitting pictures of the mulch HOWEVER you might need to crop or alter these images to make them work for our newsletter.

Project Deadline Extended
Reason: We have not yet found a design we think is Straight to the point. Simple and with our theme.

```html
<!DOCTYPE html>
<html lang="en">
<head>
<meta charset="utf-8">
<title>Varnell Contracting – Mulch Sale Newsletter</title>
<link rel="stylesheet" href="https://fonts.googleapis.com/css2?family=Arimo:wght@400;700&family=Open+Sans:wght@400;600;700&display=swap">
<style>
  :root {
    --green-dark: #0b5e0b;
    --green-deep: #0a4f0a;
    --green-lime: #7ed321;
    --green-bright: #8ee01f;
    --green-text: #126b12;
    --orange-red: #ff4a12;
    --price-red: #e8301c;
    --buy-orange: #f5a623;
    --grey-band: #efeeec;
    --ink: #111111;
    --white: #ffffff;
    --footer-bar: #1c2a10;
    --social-blue: #3a5a98;
  }
  * { box-sizing: border-box; margin: 0; padding: 0; }
  html, body { width: 1200px; height: 2639px; overflow: hidden; background: var(--white); }
  body { position: relative; font-family: "Open Sans", Arial, sans-serif; color: var(--ink); }
  .abs { position: absolute; }

  /* Header */
  .brand { left: 167px; top: 8px; height: 84px; display: flex; align-items: center; gap: 12px; }
  .brand-dot { width: 70px; height: 70px; border-radius: 50%; background: var(--green-dark); }
  .brand-name { font-weight: 700; font-size: 30px; color: var(--ink); line-height: 1; }
  .top-links { right: 168px; top: 8px; font-size: 16px; font-weight: 600; color: var(--green-dark); }
  .top-social { right: 168px; top: 42px; display: flex; gap: 14px; }
  .top-social span { width: 32px; height: 32px; border-radius: 3px; background: var(--social-blue); display: block; }
  .top-social span:nth-child(2) { background: #f08a16; }
  .top-social span:nth-child(3) { background: #2f9fe0; }
  .top-social span:nth-child(4) { background: #43a9e6; }

  .headline { left: 150px; width: 900px; top: 118px; text-align: center; font-family: "Arimo", Arial, sans-serif; font-weight: 700; font-size: 57px; letter-spacing: 0.5px; }
  .headline .mulch { color: var(--green-dark); }
  .headline .sale { color: var(--green-lime); }

  .hero { left: 150px; top: 188px; width: 900px; height: 457px;
    background: linear-gradient(100deg, #5a6a30 0%, #3b3326 28%, #9a9a92 40%, #b7b6ad 50%, #2f2820 62%, #5f8a2a 78%, #7fa63a 100%); }

  /* Order band */
  .order-band { left: 150px; top: 645px; width: 900px; height: 150px; background: var(--grey-band); }
  .order-btn { left: 167px; top: 659px; width: 392px; height: 107px; border-radius: 9px;
    background: linear-gradient(#1f8a1a, #0b5e0b); text-align: center; padding-top: 10px; }
  .order-btn .main { display: block; font-size: 43px; font-weight: 600; color: var(--green-bright); line-height: 1.1; }
  .order-btn .sub { display: block; font-size: 27px; color: var(--white); line-height: 1.3; }
  .starts { left: 596px; top: 656px; font-family: "Arimo", Arial, sans-serif; font-size: 54px; line-height: 1.08; }
  .starts .price { color: var(--orange-red); }

  /* Divisions */
  .division { top: 806px; width: 204px; height: 376px; }
  .division-head { height: 91px; background: var(--green-dark); border-bottom: 5px solid var(--green-lime);
    color: var(--white); font-weight: 600; font-size: 24px; line-height: 1.15; text-align: center; padding-top: 16px; }
  .division-photo { height: 285px; }
  .d1 { left: 158px; } .d1 .division-photo { background: linear-gradient(#a7c07a, #3f6a20); }
  .d2 { left: 385px; } .d2 .division-photo { background: linear-gradient(#c9d7e6, #eef2f6 60%, #b8bcc2); }
  .d3 { left: 612px; } .d3 .division-photo { background: linear-gradient(#6f8a55, #c8d1c0 50%, #4d6b35); }
  .d4 { left: 838px; } .d4 .division-photo { background: linear-gradient(90deg, #d8d8d8, #f2c317 55%, #c4a07a); }

  /* Products */
  .products-band { left: 150px; top: 1181px; width: 900px; height: 409px; background: var(--grey-band); }
  .card { top: 1212px; width: 272px; height: 352px; background: var(--white); box-shadow: 0 1px 5px rgba(0,0,0,0.12); }
  .card-photo { position: absolute; left: 14px; top: 24px; width: 244px; height: 212px; border: 6px solid #f4f4f4; box-shadow: 0 0 3px rgba(0,0,0,0.35); }
  .card-title { position: absolute; left: 14px; top: 253px; font-size: 25px; }
  .card-price { position: absolute; left: 16px; top: 302px; font-size: 21px; color: var(--price-red); }
  .card-buy { position: absolute; right: 14px; top: 298px; width: 90px; height: 36px; background: var(--buy-orange);
    font-family: Georgia, serif; font-size: 15px; line-height: 36px; text-align: center; color: var(--ink); }
  .c1 { left: 170px; } .c1 .card-photo { background: linear-gradient(#8fb5d8, #3a2a20 50%, #7fa6cc); }
  .c2 { left: 461px; } .c2 .card-photo { background: linear-gradient(#4f7a35, #2c2118 60%, #9a8f85); }
  .c3 { left: 751px; } .c3 .card-photo { background: linear-gradient(135deg, #a07a55, #6a4a30 50%, #b89470); }

  /* Promo */
  .promo { left: 150px; top: 1608px; width: 900px; height: 278px; background: linear-gradient(90deg, #2b2a25, #3a3d2c 55%, #4a4a44); }
  .promo-title { left: 172px; top: 1630px; font-size: 42px; font-weight: 600; color: var(--green-bright); }
  .promo-old { left: 256px; top: 1710px; font-size: 22px; color: var(--white); text-decoration: line-through; }
  .promo-new { left: 230px; top: 1754px; font-size: 23px; font-weight: 600; color: var(--green-bright); }
  .promo-btn { left: 274px; top: 1817px; width: 238px; height: 56px; border-radius: 4px; background: linear-gradient(#1f8a1a, #0b5e0b);
    color: var(--white); font-size: 23px; font-weight: 600; text-align: center; line-height: 56px; }
  .promo-pics { left: 680px; top: 1630px; }

  /* Badges */
  .badges { left: 150px; top: 1889px; width: 900px; height: 168px; background: var(--grey-band); }
  .badge { top: 1948px; height: 52px; }
  .b1 { left: 165px; width: 165px; background: #3f6fb0; border-radius: 26px; }
  .b2 { left: 398px; width: 138px; background: #222222; }
  .b3 { left: 598px; width: 140px; background: #1d5ea8; border-radius: 6px; }
  .b4 { left: 796px; width: 84px; background: #2c4d9c; border-radius: 50%; }
  .b5 { left: 932px; width: 52px; background: #f2a81d; border-radius: 50%; }

  /* Conditions */
  .cond-title { left: 150px; width: 900px; top: 2066px; text-align: center; font-size: 32px; font-weight: 400; }
  .cond-sub { left: 150px; width: 900px; top: 2117px; text-align: center; font-size: 21px; color: var(--green-text); }
  .mulch-col { top: 2168px; font-size: 20px; line-height: 36px; color: var(--green-text); }
  .mulch-rule { top: 2170px; width: 1px; height: 76px; background: #cccccc; }
  .fine { left: 150px; width: 900px; top: 2261px; text-align: center; font-size: 19.5px; line-height: 36px; }

  /* Footer */
  .footer { left: 150px; top: 2354px; width: 900px; height: 233px; background: var(--green-deep); color: var(--white); text-align: center; }
  .footer-name { position: absolute; left: 0; width: 100%; top: 12px; font-size: 31px; }
  .footer-line { position: absolute; left: 0; width: 100%; font-size: 20px; }
  .footer-social { position: absolute; left: 0; width: 100%; top: 176px; display: flex; justify-content: center; gap: 12px; }
  .footer-social span { width: 32px; height: 32px; background: var(--white); display: block; }
  .bottom-bar { left: 150px; top: 2587px; width: 900px; height: 52px; background: var(--footer-bar); color: var(--white); font-size: 18px; line-height: 52px; padding-left: 20px; }
  .pay { top: 2601px; width: 40px; height: 26px; background: var(--white); border-radius: 3px; }
</style>
</head>
<body>

<header>
  <div class="abs brand"><span class="brand-dot"></span><span class="brand-name">Varnell Contracting</span></div>
  <div class="abs top-links">View It Online | Visit Our Website</div>
  <div class="abs top-social" aria-label="Social links"><span></span><span></span><span></span><span></span></div>
</header>

<h1 class="abs headline">UP TO 30% OFF <span class="mulch">MULCH</span> <span class="sale">SALE</span></h1>

<div class="abs hero" role="img" aria-label="Freshly mulched garden beds along a curved concrete walkway with lawn and shrubs"></div>

<section>
  <div class="abs order-band"></div>
  <div class="abs order-btn"><span class="main">ORDER NOW</span><span class="sub">Get Free Estimate</span></div>
  <div class="abs starts">STARTS FROM<br><span class="price">$ 125</span> PER YARD</div>
</section>

<section>
  <div class="abs division d1"><div class="division-head">LANDSCAPE<br>DIVISION</div><div class="division-photo" role="img" aria-label="Landscaped yard with trees and shrubs"></div></div>
  <div class="abs division d2"><div class="division-head">SNOW &amp; ICE<br>DIVISION</div><div class="division-photo" role="img" aria-label="Plow truck clearing a snowy street"></div></div>
  <div class="abs division d3"><div class="division-head">IRRIGATION<br>DIVISION</div><div class="division-photo" role="img" aria-label="Sprinkler watering a lawn"></div></div>
  <div class="abs division d4"><div class="division-head">ELECTRICAL<br>DIVISION</div><div class="division-photo" role="img" aria-label="Multimeter testing an electrical panel"></div></div>
</section>

<section>
  <div class="abs products-band"></div>
  <div class="abs card c1"><div class="card-photo" role="img" aria-label="Hands holding dark soil"></div><div class="card-title">Delievry Of Soils</div><div class="card-price">$125 / Yard</div><div class="card-buy">BUY NOW</div></div>
  <div class="abs card c2"><div class="card-photo" role="img" aria-label="Garden bed edged with stone pavers"></div><div class="card-title">Delievry Of Stone</div><div class="card-price">$125 / Yard</div><div class="card-buy">BUY NOW</div></div>
  <div class="abs card c3"><div class="card-photo" role="img" aria-label="Stack of split firewood"></div><div class="card-title">Delievry Of Wood</div><div class="card-price">$125 / Yard</div><div class="card-buy">BUY NOW</div></div>
</section>

<section>
  <div class="abs promo" role="img" aria-label="Dusky garden with mulched beds and shrubs"></div>
  <div class="abs promo-title">Save Up To $ 44/Yard</div>
  <div class="abs promo-old">$169/Yard installed/Delivered</div>
  <div class="abs promo-new">$125/Yard Installed &amp; Delivered</div>
  <div class="abs promo-btn">Contact Us Now</div>
  <svg class="abs promo-pics" width="300" height="240" viewBox="0 0 300 240" role="img" aria-label="Stacked photo prints of a mulched garden bed">
    <g transform="rotate(8 150 120)"><rect x="40" y="30" width="240" height="180" fill="#ffffff"/><rect x="52" y="42" width="216" height="156" fill="#6d6a5c"/></g>
    <g transform="rotate(3 150 120)"><rect x="30" y="25" width="240" height="180" fill="#ffffff"/><rect x="42" y="37" width="216" height="156" fill="#5b5a4c"/></g>
    <g transform="rotate(-6 150 120)"><rect x="20" y="20" width="240" height="180" fill="#ffffff"/><rect x="32" y="32" width="216" height="156" fill="#4a4234"/></g>
  </svg>
</section>

<section aria-label="Memberships and accreditations">
  <div class="abs badges"></div>
  <div class="abs badge b1"></div>
  <div class="abs badge b2"></div>
  <div class="abs badge b3"></div>
  <div class="abs badge b4"></div>
  <div class="abs badge b5"></div>
</section>

<section>
  <h2 class="abs cond-title">Some Conditions Apply</h2>
  <div class="abs cond-sub">Mulches included in sale</div>
  <div class="abs mulch-col" style="left:176px">Classic Cedar<br>Black Cedar</div>
  <div class="abs mulch-rule" style="left:358px"></div>
  <div class="abs mulch-col" style="left:388px">Chocolate Brown<br>Pine Bark</div>
  <div class="abs mulch-rule" style="left:598px"></div>
  <div class="abs mulch-col" style="left:665px">Red Cedar<br>Natural Shredded Pine</div>
  <div class="abs mulch-rule" style="left:900px"></div>
  <div class="abs mulch-col" style="left:930px">Hemlock<br>Utility Style</div>
  <p class="abs fine">Some site conditions may incur extra cost minimum 3 Yards for sale price to be in effect,<br>HST extra on all prices listed,</p>
</section>

<footer>
  <div class="abs footer">
    <div class="footer-name">Varnell Contracting Group</div>
    <div class="footer-line" style="top:72px">Phone: 519 555 0147</div>
    <div class="footer-line" style="top:103px">Email: info@varnellcontracting.com</div>
    <div class="footer-line" style="top:134px">Website: www.varnellcontracting.com</div>
    <div class="footer-social"><span></span><span></span><span></span><span></span></div>
  </div>
  <div class="abs bottom-bar">Varnell Contracting Group © 2014 | Privacy Policy</div>
  <div class="abs pay" style="left:944px"></div>
  <div class="abs pay" style="left:990px"></div>
</footer>

</body>
</html>
```